Letterhead Design for Law Firm that Specializes in Property Damage Litigation

We are looking for a redesign of our letterhead. Our current letterhead lists all of our current staff members and we'd like to come up with a design that does NOT list all of the staff members so that it does not need to be updated with every newly hired employee. Must be in editable format.

We are a law firm that specializes in property damage, so we need something that is professional, yet modern. The final design should use our existing logo and should use a blue color scheme (alternate colors would be gray, black, and white).

Industry/Entity Type

Legal

Colors
0054AA
0677BA
7BADD7
CADEEF
E8F1F8

```html
<!DOCTYPE html>
<html lang="en">
<head>
<meta charset="utf-8">
<title>Harrow Lindqvist &amp; Ostrand Letterhead</title>
<link href="https://fonts.googleapis.com/css2?family=Cinzel:wght@500&family=Source+Sans+3:wght@400;700&display=swap" rel="stylesheet">
<style>
  :root {
    --navy: #1b3263;
    --slate: #666768;
    --text-gray: #5a5b5d;
    --paper: #f4f4f4;
    --backdrop: #e2e3e4;
    --white: #ffffff;
  }
  html, body {
    margin: 0;
    width: 1200px;
    height: 1200px;
    overflow: hidden;
    background: var(--backdrop);
  }
  .letterhead {
    position: absolute;
    left: 233px;
    top: 125px;
    width: 734px;
    height: 950px;
    background: var(--paper);
    font-family: "Source Sans 3", Arial, sans-serif;
    color: var(--text-gray);
  }
  .contact-tabs {
    position: absolute;
    left: 0;
    top: 0;
    width: 734px;
    height: 31px;
  }
  .tab-label {
    font-family: "Source Sans 3", Arial, sans-serif;
    font-weight: 700;
    font-size: 11.5px;
    letter-spacing: 1.2px;
    fill: var(--white);
  }
  .office {
    position: absolute;
    top: 62px;
    font-size: 10px;
    line-height: 13px;
  }
  .office--nj { left: 56px; }
  .office--pa { right: 56px; text-align: right; }
  .office-title {
    font-family: "Cinzel", Georgia, serif;
    font-weight: 500;
    font-size: 12px;
    color: var(--navy);
    margin: 0 0 1px;
    letter-spacing: 0.3px;
  }
  .office-address { margin: 0 0 4px; }
  .office-line { display: flex; align-items: center; gap: 3px; }
  .office--pa .office-line { justify-content: flex-end; }
  .office-line svg { width: 9px; height: 9px; fill: var(--navy); }
  .firm-block {
    position: absolute;
    left: 0;
    right: 0;
    top: 82px;
    text-align: center;
  }
  .firm-name {
    display: inline-flex;
    align-items: center;
    gap: 8px;
    margin: 0;
    font-family: "Source Sans 3", Arial, sans-serif;
    font-weight: 700;
    font-size: 15px;
    line-height: 18px;
    letter-spacing: 1px;
    color: var(--navy);
  }
  .firm-square {
    width: 10px;
    height: 10px;
    background: var(--navy);
  }
  .firm-tagline {
    margin: 12px 0 0;
    font-weight: 700;
    font-size: 10px;
    letter-spacing: 2px;
    color: var(--slate);
  }
  .footer-band {
    position: absolute;
    left: 0;
    bottom: 0;
    width: 100%;
    height: 16px;
    background: var(--navy);
  }
</style>
</head>
<body>
  <main class="letterhead">
    <svg class="contact-tabs" viewBox="0 0 734 31" aria-label="Main phone and website">
      <polygon points="212,0 332,0 360,31 240,31" fill="var(--slate)"/>
      <polygon points="334,0 521,0 494,31 361,31" fill="var(--navy)"/>
      <text class="tab-label" x="289" y="20" text-anchor="middle">555.310.2000</text>
      <text class="tab-label" x="428" y="20" text-anchor="middle">www.hlolegal.com</text>
    </svg>

    <section class="office office--nj">
      <h2 class="office-title">NEW JERSEY OFFICE</h2>
      <p class="office-address">2210 Meadow Pike North<br>Suite 310<br>Maple Ridge, NJ 08100</p>
      <div class="office-line">
        <svg viewBox="0 0 10 10"><path d="M2 0.5 L3.6 2.6 L2.7 3.6 Q3.8 5.9 6.3 7.2 L7.3 6.3 L9.5 7.9 L8.4 9.5 Q4.5 9.5 1.8 6.4 Q0.2 4.2 0.5 1.6 Z"/></svg>
        <span>555.482.1190</span>
      </div>
      <div class="office-line">
        <svg viewBox="0 0 10 10"><rect x="2.5" y="0.5" width="5" height="3"/><rect x="0.5" y="3.5" width="9" height="4.5" rx="1"/><rect x="2.5" y="8" width="5" height="1.5"/></svg>
        <span>555.310.2099</span>
      </div>
    </section>

    <header class="firm-block">
      <h1 class="firm-name">
        <span class="firm-square"></span>
        <span>HARROW LINDQVIST &amp; OSTRAND</span>
      </h1>
      <p class="firm-tagline">COUNSEL FOR HOME AND BUSINESS CLAIMS</p>
    </header>

    <section class="office office--pa">
      <h2 class="office-title">PHILADELPHIA OFFICE</h2>
      <p class="office-address">4450 Harbor Street<br>Suite 1800<br>Philadelphia, PA 19199</p>
      <div class="office-line">
        <span>555.310.2000</span>
        <svg viewBox="0 0 10 10"><path d="M2 0.5 L3.6 2.6 L2.7 3.6 Q3.8 5.9 6.3 7.2 L7.3 6.3 L9.5 7.9 L8.4 9.5 Q4.5 9.5 1.8 6.4 Q0.2 4.2 0.5 1.6 Z"/></svg>
      </div>
      <div class="office-line">
        <span>555.310.2099</span>
        <svg viewBox="0 0 10 10"><rect x="2.5" y="0.5" width="5" height="3"/><rect x="0.5" y="3.5" width="9" height="4.5" rx="1"/><rect x="2.5" y="8" width="5" height="1.5"/></svg>
      </div>
    </section>

    <div class="footer-band"></div>
  </main>
</body>
</html>
```